facial aesthetics advertising dermal fillers for lip and facial rejuvenation

the poster(s) is to engage the interest of patients in a dental surgery. I am introducing new service and wish to attract interest and increase bookings. the service is facial rejuvenation using dermal fillers to reinstore youthfulness vitality and lost volume to the ageing female and male patients as well as to volumise lips in those patients who want fuller lips. upon seeing the poster the patient should feel positive
Updates

Reason: Looking for a client-pulling stand out design which communicates effectively the service of facial rejuvenation, restoration of vitality and returning patients their self-confidence. Graphics need to be of realistic men and women who are aged mid 30 onwards. Images should also include before and after treatments. These images can be sent over if required. Please see original brief for other details Many thanks for reading through and helping the cause.

Target Market(s)

18-65+

Industry/Entity Type

Dental

Colors

Designer to choose colors to be used in the design.

Requirements
Must have
• 1.clear images of female at forefront (perhaps male in the background looking happily at the woman) attractive features
• full lips
• age perhaps mid 30s
• 2. pre and post dermal filler treatment poster.
Nice to have
• eye catching but not brash
• sophisticated and positive

```html
<!DOCTYPE html>
<html lang="en">
<head>
<meta charset="utf-8">
<title>Pre and Post Dermal Filler Treatment</title>
<link href="https://fonts.googleapis.com/css2?family=Lato:wght@300;400;700;900&display=swap" rel="stylesheet">
<style>
  :root {
    --teal: #138a7e;
    --teal-deep: #0f7a70;
    --mint: #cdeae8;
    --mint-light: #e2f3f2;
    --mint-mid: #a9dcd8;
    --charcoal: #3b3a3d;
    --white: #ffffff;
    --label-grey: #6d6d6d;
  }
  * { margin: 0; padding: 0; box-sizing: border-box; }
  html, body { width: 1200px; height: 2400px; overflow: hidden; }
  body { font-family: 'Lato', sans-serif; background: var(--mint); }
  .poster {
    position: relative; width: 1200px; height: 2400px; overflow: hidden;
    background: linear-gradient(160deg, var(--mint-light) 0%, var(--mint) 45%, var(--mint-light) 100%);
  }
  .poster-shapes { position: absolute; inset: 0; }
  .headline span { position: absolute; line-height: 1; white-space: nowrap; }
  .hl-pre { top: 464px; left: 52px; font-size: 208px; font-weight: 900; color: var(--teal); }
  .hl-and { top: 643px; left: 232px; font-size: 120px; font-weight: 300; color: var(--charcoal); }
  .hl-post { top: 686px; left: 52px; font-size: 224px; font-weight: 900; color: var(--teal); }
  .hl-dermal { top: 942px; left: 270px; font-size: 192px; font-weight: 900; color: var(--charcoal); letter-spacing: -2px; }
  .hl-filler { top: 1089px; left: 48px; font-size: 176px; font-weight: 900; color: var(--charcoal); letter-spacing: -2px; }
  .hl-treatment { top: 1135px; left: 496px; font-size: 124px; font-weight: 900; color: var(--teal); }
  .service-band {
    position: absolute; top: 1368px; left: 0; width: 1200px; height: 184px;
    background: var(--charcoal); color: var(--white);
    display: flex; flex-direction: column; justify-content: center; align-items: center;
    font-weight: 700; font-size: 70px; line-height: 1.05; text-transform: uppercase; letter-spacing: 0.5px;
  }
  .result-label {
    position: absolute; top: 2112px; width: 288px; text-align: center;
    font-size: 16px; letter-spacing: 1.5px; color: var(--label-grey); font-weight: 700;
  }
  .label-before { left: 432px; }
  .label-after { left: 832px; }
  .contact {
    position: absolute; left: 48px; top: 2152px;
    font-size: 42px; line-height: 1.02; color: var(--charcoal); font-weight: 400;
  }
  .web-bar {
    position: absolute; left: 0; bottom: 0; width: 1200px; height: 100px;
    background: var(--teal); color: var(--white);
    display: flex; align-items: center; justify-content: center;
    font-size: 46px; font-weight: 700; letter-spacing: 13px;
  }
</style>
</head>
<body>
<main class="poster">
  <svg class="poster-shapes" width="1200" height="2400" viewBox="0 0 1200 2400" xmlns="http://www.w3.org/2000/svg">
    <defs>
      <linearGradient id="portraitTone" x1="0" y1="0" x2="1" y2="1">
        <stop offset="0" stop-color="#8fa86a"/>
        <stop offset="0.35" stop-color="#c79a78"/>
        <stop offset="0.7" stop-color="#f0c6ae"/>
        <stop offset="1" stop-color="#d9d3cc"/>
      </linearGradient>
      <linearGradient id="resultTone" x1="0" y1="0" x2="0" y2="1">
        <stop offset="0" stop-color="#e6cf9a"/>
        <stop offset="0.45" stop-color="#e7bda3"/>
        <stop offset="1" stop-color="#d9ab92"/>
      </linearGradient>
    </defs>
    <path class="soft-swoosh" d="M0 300 C300 600 200 1100 700 1500 L0 1500 Z" fill="#bfe4e1" opacity="0.6"/>
    <path class="soft-swoosh" d="M0 1700 C300 1900 500 2200 900 2300 L0 2300 Z" fill="#b6e0dc" opacity="0.5"/>
    <path class="soft-swoosh" d="M700 1450 C900 1500 1100 1560 1200 1620 L1200 1450 Z" fill="#b9e1dd" opacity="0.6"/>

    <path class="portrait-area" role="img" aria-label="Photograph of a smiling young woman with long brown hair"
      d="M608 0 C520 150 450 450 560 700 C650 880 1000 900 1200 1184 L1200 0 Z" fill="url(#portraitTone)"/>
    <path class="portrait-frame" d="M608 0 C520 150 450 450 560 700 C650 880 1000 900 1200 1184"
      fill="none" stroke="var(--teal)" stroke-width="18"/>

    <path class="results-panel" d="M1210 1612 C900 1585 420 1590 290 1650 C160 1715 150 2110 290 2160 C520 2200 900 2192 1210 2150 Z"
      fill="var(--white)" stroke="var(--teal)" stroke-width="16"/>
    <rect class="result-photo" role="img" aria-label="Before treatment: woman with short blonde hair, frown lines visible"
      x="432" y="1664" width="288" height="432" rx="120" fill="url(#resultTone)"/>
    <rect class="result-photo" role="img" aria-label="After treatment: same woman with smoother forehead"
      x="832" y="1664" width="288" height="432" rx="120" fill="url(#resultTone)"/>
  </svg>

  <h1 class="headline">
    <span class="hl-pre">pre</span>
    <span class="hl-and">and</span>
    <span class="hl-post">post</span>
    <span class="hl-dermal">dermal</span>
    <span class="hl-filler">filler</span>
    <span class="hl-treatment">treatment</span>
  </h1>

  <div class="service-band">
    <span>Anti Wrinkle Injections</span>
    <span>Dermal Fillers</span>
  </div>

  <div class="result-label label-before">BEFORE</div>
  <div class="result-label label-after">AFTER</div>

  <address class="contact" style="font-style: normal;">
    345 555 0182<br>
    Your Address here<br>
    youemail@here.com
  </address>

  <div class="web-bar">www.yourwebsitehere.com</div>
</main>
</body>
</html>
```